New Business Card Design Project

The idea, the card is to put a card, which contains two companies at the same time. Please see the attached data and idea of how the current cards are.
Updates
VELDAK
Constructora
Ferrotrac Delmar SRL.
Equipos para Plantas de Tratamientos y Acueductos, Alquiler de Equipos Pesados para la Construcción.
C / Pedro Lucena No.47
Loma Clara, Santo Domingo. República Dominicana.
Tel .: 1809 555 4172
CEL: 1829 555 6281
teodoro@ferrotracdelmar.net
veldakobras@mailvista.example
www.ferrotracdelmar.net
Veldak construction.
Es una empresa constructora.
NOTA: La idea es llevar una sola tarjeta para dos compañías. o si no resulta hacer un diseño en cada lado, uno para cada empresa.Equipos para Plantas de Tratamiento y Acueductos, Alquiler de Equipos Pesados para la Construcción.
Deben de llevar, los logos.
VELDAK
Constructora
Ferrotrac Delmar SRL.
C / Pedro Lucena No.47
Tel .: 1809 555 4172
CEL: 1829 555 6281
Veldak construction.
VELDAK
Constructora
Ferrotrac Delmar SRL.
C / Pedro Lucena No.47
Tel .: 1809 555 4172
CEL: 1829 555 6281
Veldak construction.
It is a construction company
NOTE: The idea is to carry a single card for two companies. or if it does not turn out to make a design on each side, one for each company. Equipment for Treatment Plants and Aqueducts, Rental of Heavy Equipment for Construction.
They must carry, the logos.
How is the design similar to that, send example, for data, from previous designs.
What I'm looking for is a new design, not a remodeled copy
ferrotracdelmar
Tel: 1809 555 4172
cel: 1829 555 6281
teodoro@ferrotracdelmar.net
Direccion:
C/ Pedro Lucena # 47
Loma clara, Santo Domingo
Republica Dominicana
Veldak
constructora
Tel: 1809 555-3907
Cel: 1829 555 6281
veldaksa1@mailvista.example
Direccion:
C/ Pedro Lucena # 47
Republica Dominicana
Contact Information for Business Card
FERROTRAC DELMAR, S.R.L.
C/ Tomás Benítez Olarte esquina Pedro Lucena # 47
Loma Clara, Santo Domingo, República Dominicana
Office: 809.555.4172
Fax: 809.555.8364
Cel (Local): 829 555 6281
E-mail: DUMMY@DUMMY.com
E-mail:DUMMY@gmail.com
Website: http://www.DUMMY.com
Look and feel
Each slider illustrates characteristics of the customer's brand and the style your logo design should communicate.

```html
<!DOCTYPE html>
<html lang="es">
<head>
<meta charset="utf-8">
<title>Tarjetas de presentación – Ferrotrac Delmar y Veldak</title>
<link href="https://fonts.googleapis.com/css2?family=Roboto:wght@400;500&family=Roboto+Condensed:wght@700;800&display=swap" rel="stylesheet">
<style>
  :root{
    --page:#ecebe8;
    --card:#ffffff;
    --navy:#1f2a6b;
    --ink:#1c1c2e;
    --text:#222428;
    --tagline:#2b2d7a;
    --amber:#f2a31b;
    --orange:#e8612a;
    --yellow:#fbd232;
    --steel:#3b3b3b;
    --blue:#2e7dc4;
    --deep:#1b2347;
  }
  *{margin:0;padding:0;box-sizing:border-box}
  html,body{width:900px;height:1200px;overflow:hidden;background:var(--page)}
  body{position:relative;font-family:"Roboto",Arial,sans-serif;color:var(--text)}
  .card{position:absolute;left:85px;width:733px;height:429px;background:var(--card);border-radius:22px;overflow:hidden;box-shadow:0 6px 14px rgba(0,0,0,.18)}
  .card--ferrotrac{top:143px}
  .card--veldak{top:633px}
  .abs{position:absolute}
  .brand{font-family:"Roboto Condensed",Arial,sans-serif;font-weight:800;line-height:1}
  .ferrotrac-mark{left:45px;top:45px;width:92px;height:92px;border-radius:50%;background:var(--navy)}
  .ferrotrac-name{left:144px;top:62px;font-size:26px;color:var(--navy);letter-spacing:.3px}
  .tagline{left:49px;top:139px;font-size:15.5px;line-height:24px;color:var(--tagline)}
  .splash{right:0;top:0;width:390px;height:250px;background:radial-gradient(ellipse at 65% 45%,rgba(120,140,205,.55),rgba(170,185,230,.25) 55%,rgba(255,255,255,0) 78%)}
  .person{left:49px;top:236px}
  .card--veldak .person{left:53px;top:232px}
  .person-name{font-family:"Roboto Condensed",Arial,sans-serif;font-weight:700;font-size:20px;color:var(--ink);letter-spacing:.3px}
  .person-role{font-size:16px;font-weight:500;letter-spacing:.3px;margin-top:2px}
  .card--ferrotrac .person-role{color:var(--amber)}
  .card--veldak .person-role{color:var(--orange)}
  .rule{left:49px;right:46px;height:1.5px;background:var(--navy)}
  .card--ferrotrac .rule{top:285px}
  .card--veldak .rule{top:285px;left:53px;background:#555}
  .contacts{list-style:none;left:49px;top:296px;font-size:16px;line-height:23px}
  .card--veldak .contacts{left:53px}
  .contacts li{display:flex;align-items:center;gap:9px}
  .contacts svg{width:17px;height:17px;flex:none}
  .address{right:46px;top:296px;text-align:right;font-size:16px;line-height:23px}
  .band{left:0;right:0;bottom:0;height:27px}
  .band--ferrotrac{background:linear-gradient(90deg,var(--deep),var(--blue))}
  .band--veldak{background:linear-gradient(90deg,var(--orange),var(--yellow))}
  .veldak-mark{left:55px;top:60px;width:86px;height:86px;background:var(--orange)}
  .veldak-name{left:152px;top:68px;font-size:74px;color:var(--steel)}
  .veldak-glow{right:0;top:0;width:290px;height:260px;background:linear-gradient(160deg,rgba(251,210,50,.18),rgba(232,97,42,.14))}
</style>
</head>
<body>
<svg width="0" height="0" style="position:absolute">
  <defs>
    <symbol id="icon-phone" viewBox="0 0 24 24"><path fill="currentColor" d="M6.6 10.8a15.1 15.1 0 0 0 6.6 6.6l2.2-2.2c.3-.3.7-.4 1-.2 1.1.4 2.3.6 3.6.6.6 0 1 .4 1 1V20c0 .6-.4 1-1 1A17 17 0 0 1 3 4c0-.6.4-1 1-1h3.5c.6 0 1 .4 1 1 0 1.3.2 2.5.6 3.6.1.3 0 .7-.2 1z"/></symbol>
    <symbol id="icon-mobile" viewBox="0 0 24 24"><rect x="6" y="2" width="12" height="20" rx="2" fill="none" stroke="currentColor" stroke-width="2"/><circle cx="12" cy="18.5" r="1.2" fill="currentColor"/></symbol>
    <symbol id="icon-mail" viewBox="0 0 24 24"><rect x="3" y="5" width="18" height="14" fill="currentColor"/><path d="M3 5l9 7 9-7" fill="none" stroke="#fff" stroke-width="1.6"/></symbol>
    <symbol id="icon-web" viewBox="0 0 24 24"><g fill="none" stroke="currentColor" stroke-width="1.7"><circle cx="12" cy="12" r="9"/><ellipse cx="12" cy="12" rx="4" ry="9"/><path d="M3 12h18M5 7h14M5 17h14"/></g></symbol>
  </defs>
</svg>

<section class="card card--ferrotrac">
  <div class="abs splash" role="img" aria-label="Salpicadura de agua azul"></div>
  <div class="abs ferrotrac-mark"></div>
  <div class="abs brand ferrotrac-name">FERROTRAC<br>DELMAR S.R.L</div>
  <p class="abs tagline">Equipos para Plantas de Tratamientos<br>y Acueductos, Rentas de Equipos<br>Pesados para la Construcción.</p>
  <div class="abs person">
    <div class="person-name">LIC. TEODORO SALCEDA</div>
    <div class="person-role">PRESIDENTE</div>
  </div>
  <div class="abs rule"></div>
  <ul class="abs contacts" style="color:var(--text)">
    <li><svg style="color:var(--amber)"><use href="#icon-phone"/></svg>1 809 555 4172</li>
    <li><svg style="color:var(--amber)"><use href="#icon-mobile"/></svg>1 829 555 6281</li>
    <li><svg style="color:var(--amber)"><use href="#icon-mail"/></svg>teodoro@ferrotracdelmar.net</li>
    <li><svg style="color:var(--amber)"><use href="#icon-web"/></svg>www.ferrotracdelmar.net</li>
  </ul>
  <address class="abs address" style="font-style:normal">C/ Pedro Lucena No.47<br>Loma Clara, Santo Domingo<br>Republica Dominicana</address>
  <div class="abs band band--ferrotrac"></div>
</section>

<section class="card card--veldak">
  <div class="abs veldak-glow" role="img" aria-label="Decoración suave de la marca en tonos cálidos"></div>
  <div class="abs veldak-mark"></div>
  <div class="abs brand veldak-name">VELDAK</div>
  <div class="abs person">
    <div class="person-name">LIC. TEODORO SALCEDA</div>
    <div class="person-role">PRESIDENTE</div>
  </div>
  <div class="abs rule"></div>
  <ul class="abs contacts">
    <li><svg style="color:var(--orange)"><use href="#icon-phone"/></svg>1 809 555 3907</li>
    <li><svg style="color:var(--orange)"><use href="#icon-mobile"/></svg>1 829 555 6281</li>
    <li><svg style="color:var(--orange)"><use href="#icon-mail"/></svg>veldaksa1@mailvista.example</li>
  </ul>
  <address class="abs address" style="font-style:normal">C/ Pedro Lucena No.47<br>Loma Clara, Santo Domingo<br>Republica Dominicana</address>
  <div class="abs band band--veldak"></div>
</section>
</body>
</html>
```